VIP card

I need something with the Months on it so they can be punched out. Also the wording V.I.P Card Five-Minute Hydrating Facial,
Receive a free monthly gift with this card and a $20.00 or more Cosmetic Purchase*Plus a certificate bonus yearly.
* Gift to be received in current month (in small print)

I am not sure we can get this all on one side of a business card. My card now is one sided and measures 3 1/2 by 2 1/2. I am open for suggestions. I would be open to new wording also.
Dorit

Target Market(s)

Ages 25 to 75 . Ladies that want to be pampered and look their best.

Industry/Entity Type

Business

Contact Information for Business Card

Tavish Oakley Cosmetics 487 E Corbin Rd Mexico, MO 65391 573-624-9083

Font styles to use
Serif

Requirements
Must have
• Must have months on it for punching
Nice to have
• Does not have to have a logo

```html
<!DOCTYPE html>
<html lang="en">
<head>
<meta charset="utf-8">
<title>VIP Card – Tavish Oakley Cosmetics</title>
<link rel="stylesheet" href="https://fonts.googleapis.com/css2?family=Bodoni+Moda:opsz,wght@6..96,400;6..96,500&family=Roboto+Condensed:wght@300;400&display=swap">
<style>
  :root {
    --backdrop: #e6e5ea;
    --card: #ffffff;
    --ink: #141414;
    --band-text: #d9d9d9;
    --fine-print: #8a8a8a;
    --address: #555555;
  }
  * { box-sizing: border-box; margin: 0; padding: 0; }
  html, body {
    width: 1200px;
    height: 900px;
    overflow: hidden;
    background: var(--backdrop);
  }
  .canvas {
    width: 1200px;
    height: 900px;
    display: flex;
    align-items: center;
    justify-content: center;
    gap: 40px;
  }
  .card {
    position: relative;
    width: 540px;
    height: 309px;
    background: var(--card);
    box-shadow: 3px 4px 8px rgba(0, 0, 0, 0.35);
    overflow: hidden;
  }

  /* Front */
  .front-title {
    position: absolute;
    left: 0;
    right: 0;
    top: 34px;
    text-align: center;
    font-family: "Bodoni Moda", "Didot", serif;
    font-weight: 400;
    font-size: 140px;
    line-height: 1;
    letter-spacing: -2px;
    color: var(--ink);
  }
  .front-band {
    position: absolute;
    left: 0;
    right: 0;
    top: 194px;
    height: 42px;
    background: var(--ink);
    display: flex;
    align-items: center;
    justify-content: center;
    font-family: "Roboto Condensed", "Arial Narrow", sans-serif;
    font-weight: 300;
    font-size: 21px;
    color: var(--band-text);
  }
  .front-address {
    position: absolute;
    left: 14px;
    bottom: 22px;
    font-family: "Roboto Condensed", "Arial Narrow", sans-serif;
    font-weight: 300;
    font-size: 10.5px;
    color: var(--address);
  }

  /* Back */
  .back-label {
    position: absolute;
    left: 17px;
    top: 16px;
    font-family: "Bodoni Moda", "Didot", serif;
    font-size: 17px;
    color: var(--ink);
  }
  .back-band {
    position: absolute;
    left: 0;
    right: 0;
    top: 48px;
    height: 34px;
    background: var(--ink);
    display: flex;
    align-items: center;
    justify-content: center;
    font-family: "Roboto Condensed", "Arial Narrow", sans-serif;
    font-weight: 300;
    font-size: 14.5px;
    color: var(--band-text);
  }
  .month-grid {
    position: absolute;
    left: 28px;
    top: 105px;
    display: grid;
    grid-template-columns: repeat(4, 109px);
    grid-auto-rows: 50px;
    column-gap: 17px;
    row-gap: 10px;
    list-style: none;
  }
  .month {
    background: var(--ink);
    border-radius: 25px;
    display: flex;
    align-items: center;
    justify-content: center;
    font-family: "Bodoni Moda", "Didot", serif;
    font-weight: 500;
    font-size: 18px;
    letter-spacing: 0.5px;
    color: var(--card);
  }
  .fine-print {
    position: absolute;
    left: 12px;
    bottom: 10px;
    display: flex;
    gap: 22px;
    font-family: "Roboto Condensed", "Arial Narrow", sans-serif;
    font-weight: 300;
    font-size: 8.5px;
    color: var(--fine-print);
  }
</style>
</head>
<body>
<main class="canvas">
  <section class="card card-front">
    <h1 class="front-title">VIP</h1>
    <div class="front-band">Five-Minute Hydrating Facial</div>
    <p class="front-address">Tavish Oakley Cosmetics 487 E Corbin Rd Mexico, MO 65391 573-624-9083</p>
  </section>

  <section class="card card-back">
    <p class="back-label">VIP</p>
    <div class="back-band">Receive a free monthly gift with this card and a $20.00 or more Cosmetic Purchase</div>
    <ul class="month-grid">
      <li class="month">JAN</li>
      <li class="month">FEV</li>
      <li class="month">MAR.</li>
      <li class="month">APR.</li>
      <li class="month">MAY</li>
      <li class="month">JUNE</li>
      <li class="month">JULY</li>
      <li class="month">AUG</li>
      <li class="month">SEPT</li>
      <li class="month">OCT</li>
      <li class="month">NOV</li>
      <li class="month">DEC</li>
    </ul>
    <div class="fine-print">
      <span>* Plus a certificate bonus yearly</span>
      <span>* Gift to be received in current month</span>
    </div>
  </section>
</main>
</body>
</html>
```